Beauty website banner

We are an Australian beauty website selling mid and high end cosmetics and beauty products.

We need a banner that tells customers they can share their product wishlists with friends to let them know what they want for Christmas.

Target Market(s)

Female, 30-60, white collar

Industry/Entity Type

Cosmetics

Requirements
Must have
• 600 x 150 pixels in size

Words to be as follows, not including the (") of course.

"Share your wishlist with friends and family for Christmas!"

(Then in smaller font) "Just log in to your account, go to your wishlist and click on the ‘share wishlist’ button"

```html
<!DOCTYPE html>
<html lang="en">
<head>
<meta charset="utf-8">
<title>Share Your Wishlist for Christmas</title>
<link href="https://fonts.googleapis.com/css2?family=Josefin+Sans:wght@700&family=Architects+Daughter&display=swap" rel="stylesheet">
<style>
  :root {
    --banner-pink: #f6a9f3;
    --banner-pink-light: #f9c6f6;
    --skin-light: #f6eeee;
    --skin-white: #fdfbfb;
    --lash-teal: #3e6f6c;
    --headline-red: #c8102e;
    --headline-red-dark: #7e0a1d;
    --body-ink: #1a1a1a;
  }
  html, body {
    margin: 0;
    padding: 0;
    overflow: hidden;
    background: #ffffff;
  }
  .wishlist-banner {
    position: relative;
    width: 1200px;
    height: 300px;
    overflow: hidden;
    background: linear-gradient(90deg, var(--banner-pink) 0%, var(--banner-pink) 55%, var(--banner-pink-light) 68%, var(--skin-light) 82%, var(--skin-white) 100%);
  }
  .beauty-photo {
    position: absolute;
    top: 0;
    right: 0;
    width: 480px;
    height: 300px;
    background:
      radial-gradient(ellipse 55% 14% at 38% 30%, rgba(62, 111, 108, 0.35), rgba(62, 111, 108, 0) 70%),
      linear-gradient(90deg, rgba(246, 169, 243, 0) 0%, rgba(246, 238, 238, 0.85) 35%, var(--skin-white) 100%);
  }
  .headline {
    position: absolute;
    top: 28px;
    left: 30px;
    width: 720px;
    margin: 0;
    font-family: "Josefin Sans", sans-serif;
    font-weight: 700;
    font-variant: small-caps;
    font-size: 34px;
    line-height: 60px;
    letter-spacing: 0.5px;
    text-align: center;
    color: var(--headline-red);
    text-shadow: 1px 1px 0 var(--headline-red-dark);
  }
  .instructions {
    position: absolute;
    top: 178px;
    left: 40px;
    width: 880px;
    margin: 0;
    font-family: "Architects Daughter", cursive;
    font-size: 27px;
    line-height: 36px;
    text-align: center;
    color: var(--body-ink);
  }
  .instructions span {
    display: block;
  }
  .instructions .step-intro {
    padding-left: 40px;
    text-align: left;
    margin-left: 210px;
  }
</style>
</head>
<body>
  <main class="wishlist-banner">
    <div class="beauty-photo" role="img" aria-label="Close-up photograph of a woman's closed eye with long teal lashes on pale skin"></div>
    <h1 class="headline">Share your wishlist with friends and family<br>for Christmas!</h1>
    <p class="instructions">
      <span class="step-intro">Just log in to your account</span>
      <span class="step-detail">go to your wishlist and click on the ‘share wishlist’ button</span>
    </p>
  </main>
</body>
</html>
```